Auction Company Wordpress Design Project

We need a WordPress design/concept for an established auctioneering company specializing in Benefit Auctions, Estate Auctions, Business Liquidations/Overstocks, and real estate marketing in the Chicago area. The winning design will have a professional look appealing to clients searching for these services.

Industry/Entity Type

Real Estate

Requirements
Must have
• - We will require winning designer to provide a layered PSD (Adobe photoshop) concept file, along with any non-standard font files used.

The site's navigation: 1) Home, 2) Auctions, 3) About Us, 4) Buyers, 5) Sellers, 6) Media, 7) Contact Us. Horizontal structure preferred.

A slideshow element will be represented (choice of files attached) preferably in the header. The following widgets will also be incorporated into sidebar (or other creative placement):
- Steady Relay email signup
- Featured Auctions (example shown in http://www.bidplainfield.example/ as "Upcoming Auctions" widget)
- Clipvane video widget
- Social media widget for Pallroom, Chirble, Clipvane icons
- Testimonials widget

Winning design will creatively use colors in logo (with perhaps accent color) with a professional, clean look. Client mentions liking the use of color in http://www.lotvistara.example/

Footer of site will have generic contact info (phone number, email addresses, mailing address; a smaller instance of logo; and the attached association logos.
Nice to have
• - Use of drop-down menus should be demonstrated by incorporating mouse-over for 1) Upcoming, 2) Online, 3) Past, under the 'Auctions' main menu item (for clarity of design, this drop-down can be placed under any other menu item if necessary).
Should not have
• Please do not use auction gavels in the design.

```html
<!DOCTYPE html>
<html lang="en">
<head>
<meta charset="utf-8">
<title>Lakeshore Bidding Realty</title>
<link rel="stylesheet" href="https://fonts.googleapis.com/css2?family=Cinzel:wght@400;600&family=Open+Sans:wght@400;600;700&family=Source+Sans+3:wght@400;600&family=Questrial&display=swap">
<style>
:root{
  --band-dark:#332e29;
  --band-mid:#4a443d;
  --nav-grey:#5d636a;
  --orange:#f07a1a;
  --maroon:#7a1414;
  --link-blue:#1e6fd6;
  --ink:#222;
  --text:#3a3a3a;
  --tab:#2f2c29;
  --card-shadow:rgba(0,0,0,.35);
  --field:#e2e2e2;
  --badge:#9a9a9a;
}
*{box-sizing:border-box;margin:0;padding:0}
html,body{width:1052px;height:1200px;overflow:hidden;background:#fff}
.stage{position:relative;width:1000px;height:1125px;transform:scale(1.052,1.0667);transform-origin:0 0;
  background:linear-gradient(#8f8a83 80px,#b5b1ab 300px,#d3d1cd 520px,#fff 640px);font-family:"Open Sans",sans-serif;overflow:hidden}
.abs{position:absolute}
.top-band{left:0;top:0;width:1000px;height:80px;background:linear-gradient(var(--band-dark),var(--band-mid))}
.main-nav{left:0;top:78px;width:998px;height:30px;background:var(--nav-grey);border-bottom:1px solid #3f4449}
.main-nav a{position:absolute;top:8px;font-family:"Cinzel",serif;font-size:13px;color:#fff;text-decoration:none;letter-spacing:.3px}
.brand-box{left:446px;top:0;width:108px;height:105px;background:#fff;border:1px solid #999;box-shadow:0 2px 4px rgba(0,0,0,.4);
  display:flex;flex-direction:column;align-items:center;justify-content:center;text-align:center;gap:6px}
.brand-mark{width:14px;height:14px;background:#6b6660}
.brand-name{font-family:"Cinzel",serif;font-weight:600;font-size:13px;line-height:1.15;color:#4a4640}
.newsletter{font-family:"Questrial",sans-serif;color:var(--orange);line-height:.95}
.newsletter .small{font-size:14px;display:block}
.newsletter .big{font-size:22px;display:block}
.field{background:var(--field);border:1px solid #bbb}
.go{background:#d8d8d8;border:1px solid #999;display:flex;align-items:center;justify-content:center}
.social{display:flex;gap:3px}
.social span{width:16px;height:16px;background:#8c8780;border-radius:2px}
.content-panel{left:110px;top:108px;width:770px;height:810px;border:1px solid #e3e3e3;border-top:none;border-radius:0 0 18px 18px;background:linear-gradient(rgba(255,255,255,0) 450px,#fff 600px)}
.hero{left:120px;top:113px;width:750px;height:193px;background:linear-gradient(110deg,#5d6f8a 0%,#c9c2b6 35%,#e9d9b4 55%,#6f6a5c 80%,#3c3a33 100%)}
.featured{left:684px;top:120px;width:180px;height:178px;background:#d7d4cd;border:1px solid #bfbab2}
.featured h3{font-family:"Cinzel",serif;font-weight:400;font-size:12.5px;color:#fff;text-align:center;margin-top:8px;text-shadow:0 1px 1px rgba(0,0,0,.3)}
.featured .thumb{position:absolute;left:11px;top:28px;width:156px;height:103px;background:linear-gradient(#3b9be0 0 45%,#a33a2a 45% 62%,#7fb23a 62%)}
.featured p{position:absolute;left:6px;top:136px;width:168px;font-size:9.5px;font-weight:700;line-height:1.2;text-align:center;color:#111}
.section-tab{height:21px;background:var(--tab);color:#fff;font-family:"Source Sans 3",sans-serif;font-size:14px;padding:1px 0 0 28px;border-radius:0 8px 8px 0;box-shadow:0 1px 2px rgba(0,0,0,.5)}
.card{background:#fff;box-shadow:0 1px 4px var(--card-shadow)}
.listing{width:530px;height:96px}
.listing .thumb{position:absolute;left:13px;top:8px;width:79px;height:80px;border-radius:8px;background:linear-gradient(#cfd6dc,#a5a8a6 60%,#8b7a5e)}
.listing .body{position:absolute;left:103px;top:8px;width:412px}
.listing h4{font-family:"Source Sans 3",sans-serif;font-weight:600;font-size:13px;color:var(--orange);line-height:15px}
.listing p{font-size:7.5px;line-height:10.5px;color:var(--text)}
.listing .meta{font-size:9px;font-weight:600;color:var(--ink);margin-top:3px}
.listing .meta b{color:var(--maroon);font-weight:600}
.listing .meta b+span{margin-right:12px}
.listing .actions{position:absolute;right:16px;bottom:6px;font-size:9.5px;font-weight:600;color:var(--link-blue);word-spacing:0}
.listing .actions span+span{margin-left:10px}
.video{left:676px;top:350px;width:185px;height:115px;background:radial-gradient(circle at 30% 35%,#b49b6a,#3d3326 70%)}
.video .bar{position:absolute;left:0;bottom:0;width:100%;height:9px;background:#1a1a1a}
.quote{position:absolute;left:20px;width:170px;font-size:8px;line-height:11px;color:var(--text);padding:8px 12px 0 12px}
.quote::before{content:"\201C";position:absolute;left:0;top:-8px;font-size:30px;color:#bbb;font-family:Georgia,serif}
.quote::after{content:"\201D";position:absolute;right:-10px;bottom:-20px;font-size:30px;color:#bbb;font-family:Georgia,serif}
.follow-row{position:absolute;left:10px;display:flex;gap:14px;align-items:flex-start}
.follow-row .sq{width:44px;height:44px;background:#d9d6d0}
.follow-row .nm{font-family:"Source Sans 3",sans-serif;font-size:14px;line-height:13px;color:#333}
.like{display:inline-block;margin-top:6px;font-size:7px;color:#999;border:1px solid #ccc;padding:2px 4px;background:#f4f4f4}
.scrollbar{left:855px;top:777px;width:11px;height:110px;background:#f1f1f1;border:1px solid #ccc}
.scrollbar span{position:absolute;left:1px;top:12px;width:7px;height:12px;background:#7ea7d9}
.badge{background:var(--badge)}
.footer-nav{left:250px;top:1064px;width:510px;font-family:"Questrial",sans-serif;font-size:10px;color:#666}
.footer-nav span{position:absolute}
.copyright{left:0;top:1092px;width:1000px;text-align:center;font-size:8px;font-weight:700;color:#111}
.chevron{stroke:#fff;stroke-width:2;fill:none}
</style>
</head>
<body>
<div class="stage">

  <div class="abs top-band"></div>
  <nav class="abs main-nav">
    <a style="left:145px">Home</a><a style="left:203px">Auctions</a><a style="left:292px">About Us</a><a style="left:382px">Buyers</a>
    <a style="left:581px">Sellers</a><a style="left:660px">Media</a><a style="left:739px">Contact Us</a>
  </nav>

  <div class="abs brand-box"><span class="brand-mark"></span><span class="brand-name">Lakeshore<br>Bidding<br>Realty</span></div>

  <div class="abs newsletter" style="left:569px;top:42px"><span class="small">Sign Up To Our</span><span class="big">Newsletter</span></div>
  <div class="abs field" style="left:697px;top:47px;width:146px;height:21px"></div>
  <div class="abs go" style="left:846px;top:47px;width:20px;height:21px"><svg width="12" height="10"><path d="M1 5l3.5 3.5L11 1" stroke="#555" stroke-width="2" fill="none"/></svg></div>
  <div class="abs social" style="left:775px;top:12px"><span></span><span></span><span></span><span></span></div>

  <div class="abs content-panel"></div>

  <div class="abs hero" role="img" aria-label="Two-storey suburban house at dusk with lit windows and garden plants"></div>
  <svg class="abs" style="left:90px;top:190px" width="14" height="42"><path class="chevron" d="M12 1L2 21l10 20"/></svg>
  <svg class="abs" style="left:884px;top:190px" width="14" height="42"><path class="chevron" d="M2 1l10 20L2 41"/></svg>

  <aside class="abs featured">
    <h3>Featured Auctions</h3>
    <div class="thumb" role="img" aria-label="Red barns and silos beside a green field under blue sky"></div>
    <p>Lorem ipsum dolor sit amet, consectetur adipiscing elit.</p>
  </aside>

  <div class="abs section-tab" style="left:107px;top:312px;width:175px">Real Estate Lisitings</div>
  <div class="abs section-tab" style="left:706px;top:312px;width:177px">Video Tour</div>

  <article class="abs card listing" style="left:124px;top:340px">
    <div class="thumb" role="img" aria-label="Two grain silos on farmland"></div>
    <div class="body"><h4>Auction Title</h4>
      <p>Lorem ipsum dolor sit amet, consectetur adipiscing elit. Fusce at eros a ligula vestibulum semper. Proin est lorem, tincidunt vel lobortis et, dapibus vel enim. In dolor turpis, consequat ac congue commodo, egestas sed dui. In eget tortor nec lectus faucibus rhoncus et sed magna.</p>
      <div class="meta"><b>Auction Begins</b> : Monday, February 04, 2013 at 10:00 AM CST</div>
      <div class="meta"><b>Seller</b> : <span>Seller Name</span> <b>Location</b> : Location Name</div></div>
    <div class="actions"><span>View Photo</span><span>More Details</span></div>
  </article>

  <article class="abs card listing" style="left:124px;top:449px">
    <div class="thumb" role="img" aria-label="Two grain silos on farmland"></div>
    <div class="body"><h4>Auction Title</h4>
      <p>Lorem ipsum dolor sit amet, consectetur adipiscing elit. Fusce at eros a ligula vestibulum semper. Proin est lorem, tincidunt vel lobortis et, dapibus vel enim. In dolor turpis, consequat ac congue commodo, egestas sed dui. In eget tortor nec lectus faucibus rhoncus et sed magna.</p>
      <div class="meta"><b>Auction Begins</b> : Monday, February 04, 2013 at 10:00 AM CST</div>
      <div class="meta"><b>Seller</b> : <span>Seller Name</span> <b>Location</b> : Location Name</div></div>
    <div class="actions"><span>View Photo</span><span>More Details</span></div>
  </article>

  <article class="abs card listing" style="left:124px;top:560px">
    <div class="thumb" role="img" aria-label="Two grain silos on farmland"></div>
    <div class="body" style="top:26px">
      <p>Lorem ipsum dolor sit amet, consectetur adipiscing elit. Fusce at eros a ligula vestibulum semper. Proin est lorem, tincidunt vel lobortis et, dapibus vel enim. In dolor turpis, consequat ac congue commodo, egestas sed dui. In eget tortor nec lectus faucibus rhoncus et sed magna.</p>
      <div class="meta"><b>Auction Begins</b> : Monday, February 04, 2013 at 10:00 AM CST</div></div>
    <div class="actions"><span>View Photo</span><span>More Details</span></div>
  </article>

  <article class="abs card listing" style="left:124px;top:673px">
    <div class="thumb" role="img" aria-label="Two grain silos on farmland"></div>
    <div class="body"><h4>Auction Title</h4>
      <p>Lorem ipsum dolor sit amet, consectetur adipiscing elit. Fusce at eros a ligula vestibulum semper. Proin est lorem, tincidunt vel lobortis et, dapibus vel enim. In dolor turpis, consequat ac congue commodo, egestas sed dui. In eget tortor nec lectus faucibus rhoncus et sed magna.</p>
      <div class="meta"><b>Auction Begins</b> : Monday, February 04, 2013 at 10:00 AM CST</div>
      <div class="meta"><b>Seller</b> : Seller Name</div></div>
    <div class="actions"><span>View Photo</span><span>More Details</span></div>
  </article>

  <article class="abs card listing" style="left:124px;top:785px">
    <div class="thumb" role="img" aria-label="Two grain silos on farmland"></div>
    <div class="body"><h4>Auction Title</h4>
      <p>Lorem ipsum dolor sit amet, consectetur adipiscing elit. Fusce at eros a ligula vestibulum semper. Proin est lorem, tincidunt vel lobortis et, dapibus vel enim. In dolor turpis, consequat ac congue commodo, egestas sed dui. In eget tortor nec lectus faucibus rhoncus et sed magna.</p>
      <div class="meta"><b>Auction Begins</b> : Monday, February 04, 2013 at 10:00 AM CST</div>
      <div class="meta"><b>Seller</b> : Seller Name</div></div>
    <div class="actions"><span>View Photo</span><span>More Details</span></div>
  </article>

  <div class="abs card" style="left:664px;top:340px;width:207px;height:134px"></div>
  <div class="abs video" role="img" aria-label="Video tour: company representative speaking in an office">
    <svg class="abs" style="left:80px;top:42px" width="24" height="24"><rect width="24" height="24" rx="4" fill="rgba(255,255,255,.35)"/><path d="M9 6l8 6-8 6z" fill="#fff"/></svg>
    <div class="bar"></div>
  </div>

  <div class="abs section-tab" style="left:706px;top:483px;width:177px">Testimonials</div>
  <div class="abs card" style="left:664px;top:508px;width:207px;height:180px">
    <p class="quote" style="top:18px">Lorem ipsum dolor sit amet, consectetur adipiscing elit.Lorem ipsum dolor sit amet, consectetur adipiscing elit.</p>
    <p class="quote" style="top:71px">Lorem ipsum dolor sit amet, consectetur adipiscing elit.Lorem ipsum dolor sit amet, consectetur adipiscing elit.</p>
    <p class="quote" style="top:124px">Lorem ipsum dolor sit amet, consectetur adipiscing elit.Lorem ipsum dolor sit amet, consectetur adipiscing elit.</p>
  </div>

  <div class="abs section-tab" style="left:706px;top:700px;width:177px">Follow Us</div>
  <div class="abs card" style="left:664px;top:729px;width:207px;height:159px">
    <div class="follow-row" style="top:12px"><span class="sq"></span><div><div class="nm">Lakeshore<br>Bidding</div><span class="like">&#10003; Like</span></div></div>
    <div class="follow-row" style="top:82px"><span class="sq"></span><div class="nm">Lakeshore<br>Bidding</div></div>
  </div>
  <div class="abs scrollbar"><span></span></div>

  <footer>
    <div class="abs social" style="left:795px;top:932px"><span></span><span></span><span></span><span></span></div>
    <div class="abs" style="left:140px;top:960px;width:110px;text-align:center;display:flex;flex-direction:column;align-items:center;gap:6px">
      <span class="brand-mark"></span><span class="brand-name" style="font-size:15px">Lakeshore<br>Bidding<br>Realty</span>
    </div>
    <div class="abs newsletter" style="left:296px;top:998px"><span class="small">Sign Up To Our</span><span class="big">Newsletter</span></div>
    <div class="abs field" style="left:433px;top:1003px;width:145px;height:22px;border:none"></div>
    <div class="abs go" style="left:581px;top:1003px;width:20px;height:22px"><svg width="12" height="10"><path d="M1 5l3.5 3.5L11 1" stroke="#555" stroke-width="2" fill="none"/></svg></div>
    <div class="abs badge" style="left:680px;top:968px;width:50px;height:62px;border-radius:4px"></div>
    <div class="abs badge" style="left:752px;top:966px;width:48px;height:64px;border-radius:50%"></div>
    <div class="abs badge" style="left:818px;top:966px;width:58px;height:58px"></div>
    <nav class="abs footer-nav">
      <span style="left:1px">Home</span><span style="left:57px">Auctions</span><span style="left:133px">Auctione</span><span style="left:212px">About Us</span>
      <span style="left:291px">Buyers</span><span style="left:343px">Sellers</span><span style="left:396px">Media</span><span style="left:449px">Contact Us</span>
    </nav>
    <p class="abs copyright">Copyright © 2007 - 2013 - Lakeshore Bidding Realty, - All Rights Reserved.</p>
  </footer>

</div>
</body>
</html>
```